Cutaneous Learning Clinical Treatments workbook New Word Template Design Project

Cutaneous Learning needs the old "Harbourview Derma Procedures Handbook" updated and given a fresh new look, using the new Cutaneous Learning logo.

The old workbook will be supplied to act as a guideline, but we'd like a fresh new look.

Target Market(s)

The people using this workbook are Dermal therapists and Dermal nurses.

Font styles to use
Serif
Sans Serif

Requirements
Must have
• The new logo incorporated on each page - obviously on the cover it will be a major focus, but on other pages we'd like to see the logo represented in a smaller way somehow.

Each module is to follow the same formula - as per the old workbook.

A4 portrait - 210mm X 297mm (8-1/4 X 11-3/4 inches)

The end result will be printed, so there must be space on the LH side to allow for binding
Nice to have
• We'd like the colour scheme of the new design to work in/match with the colour scheme of the logo.

Request from my boss - the final products we will need back are:
(1) an editable "in design" file
(2) pdf document

```html
<!DOCTYPE html>
<html lang="en">
<head>
<meta charset="utf-8">
<title>Cutaneous Learning – Clinical Treatments Workbook</title>
<link href="https://fonts.googleapis.com/css2?family=Open+Sans:ital,wght@0,400;0,600;0,700;1,400;1,600&display=swap" rel="stylesheet">
<style>
:root{
  --bg:#d9d9d9;
  --paper:#ffffff;
  --navy:#1b2160;
  --gold:#c9a449;
  --ink:#4a4a4a;
  --row-tint:#eef5f2;
  --rule:#b9bcd6;
  --note-box:#d5d6d8;
}
*{box-sizing:border-box;margin:0;padding:0}
html,body{width:1200px;height:1200px;overflow:hidden}
body{background:var(--bg);font-family:"Open Sans",sans-serif;color:var(--ink);position:relative}
.page{position:absolute;width:393px;height:497px;background:var(--paper);box-shadow:0 6px 14px rgba(0,0,0,.22);overflow:hidden}
.page--cover{left:168px;top:79px}
.page--toc-a{left:601px;top:81px}
.page--toc-b{left:166px;top:640px}
.page--intro{left:601px;top:640px}

.dots-field{position:absolute;right:0;top:0;width:260px;height:70px;background:linear-gradient(200deg,rgba(235,235,235,.7),rgba(255,255,255,0) 70%)}
.cover-dots{position:absolute;right:0;top:0;width:230px;height:200px;background:radial-gradient(ellipse at 100% 0%,rgba(231,214,170,.55),rgba(255,255,255,0) 70%)}
.cover-waves{position:absolute;left:0;top:0;width:160px;height:100%;background:linear-gradient(90deg,rgba(244,236,214,.9) 0%,rgba(207,226,238,.9) 45%,rgba(255,255,255,0) 100%)}

.brand{position:absolute;left:131px;top:135px;width:230px;text-align:center}
.brand__mark{width:52px;height:52px;border-radius:50%;background:var(--navy);margin:0 auto 14px}
.brand__name{font-weight:600;font-size:13.5px;letter-spacing:.8px;color:var(--navy);text-transform:uppercase;white-space:nowrap}

.cover-title{position:absolute;left:174px;top:288px;font-weight:600;font-size:26.5px;line-height:28px;color:var(--navy);letter-spacing:.2px}
.cover-rule{position:absolute;left:174px;top:376px;width:164px;height:1px;background:var(--navy)}
.cover-sub{position:absolute;left:174px;top:387px;font-size:7.5px;font-weight:700;letter-spacing:7.2px;color:var(--navy)}
.staff{position:absolute;left:150px;top:470px;font-size:7px;font-weight:600;color:var(--navy);display:flex;align-items:flex-end}
.staff span{display:inline-block;width:180px;border-bottom:1px solid var(--navy);margin-left:2px}

.toc-title{position:absolute;left:0;right:0;font-weight:600;font-size:28px;color:var(--navy);text-align:center}
.toc-list{position:absolute;list-style:none}
.toc-list li{display:flex;justify-content:space-between;align-items:center;font-size:7.6px;font-weight:700;color:#222;padding:0 18px 0 7px;height:16.25px;white-space:nowrap}
.toc-list .toc-head{height:22px;align-items:flex-start}

.page--toc-a .toc-title{top:92px;transform:translateY(-50%)}
.page--toc-a .toc-list{left:36px;top:129px;width:331px}
.page--toc-a .toc-list li:nth-child(odd):not(.toc-head){background:var(--row-tint)}
.page--toc-b .toc-title{top:59px;transform:translateY(-50%)}
.page--toc-b .toc-list{left:32px;top:134px;width:336px}
.page--toc-b .toc-list li{height:16.7px}
.page--toc-b .toc-list li:nth-child(even){background:var(--row-tint)}

.folio{position:absolute;left:24px;bottom:8px;right:0;display:flex;align-items:center;font-size:11px;font-weight:700;color:var(--navy)}
.folio::after{content:"";flex:1;height:1px;background:var(--rule);margin-left:6px;margin-top:4px}

.intro-title{position:absolute;left:34px;top:30px;font-size:18px;font-weight:600;color:var(--navy)}
.intro-body{position:absolute;left:32px;top:56px;width:324px;font-size:9.4px;line-height:11.6px;text-align:justify;hyphens:auto;-webkit-hyphens:auto;color:#505050}
.intro-body p{margin-bottom:9px}
.intro-body .note{font-style:italic;font-weight:600;color:#333}
.howto{position:absolute;left:23px;top:361px;width:343px;height:98px;background:var(--note-box);padding:6px 6px;font-style:italic;font-size:8.7px;color:#333}
.howto h3{font-size:7.8px;font-weight:600;color:var(--navy);margin-bottom:2px}
.howto li{list-style:none;display:flex;align-items:center;gap:4px;height:14px;white-space:nowrap}
.howto li::before{content:"";flex:0 0 7px;height:5px;background:var(--gold);border-radius:1px}
</style>
</head>
<body>

<section class="page page--cover">
  <div class="cover-waves" role="img" aria-label="Flowing blue and gold line waves"></div>
  <div class="cover-dots" role="img" aria-label="Fading gold dot pattern"></div>
  <div class="brand">
    <div class="brand__mark"></div>
    <div class="brand__name">Cutaneous Learning</div>
  </div>
  <h1 class="cover-title">CLINICAL<br>TREATMENTS<br>WORKBOOK</h1>
  <div class="cover-rule"></div>
  <div class="cover-sub">DERMATOLOGISTS</div>
  <div class="staff">STAFF NAME:<span></span></div>
</section>

<section class="page page--toc-a">
  <div class="dots-field" role="img" aria-label="Faint grey dot pattern"></div>
  <h2 class="toc-title">TABLE OF CONTENTS</h2>
  <ul class="toc-list">
    <li class="toc-head">INTRODUCTION</li>
    <li><span>WORKBOOK SUMMARY</span><span>3</span></li>
    <li><span>MODULE 1:&nbsp; DOCUMENTATION FOR TREATMENTS</span><span>4</span></li>
    <li><span>MODULE 2:&nbsp; MEDICAL PHOTOGRAPHY</span><span>5</span></li>
    <li><span>MODULE 3:&nbsp; INFECTION PREVENTION &amp; CONTROL</span><span>18</span></li>
    <li><span>MODULE 4:&nbsp; STERILISATION</span><span>26</span></li>
    <li><span>MODULE 5:&nbsp; WORKSPACE MAINTENANCE</span><span>33</span></li>
    <li><span>MODULE 6:&nbsp; PATHOLOGY COLLECTION</span><span>40</span></li>
    <li><span>MODULE 7:&nbsp; DRUGS &amp; POISONS REGULATION</span><span>47</span></li>
    <li><span>MODULE 8:&nbsp; PRE-OP CALLS TO PATIENTS</span><span>48</span></li>
    <li><span>MODULE 9:&nbsp; ADMINISTERING NUMBING CREAM</span><span>49</span></li>
    <li><span>MODULE 10: FOLLOWING UP YOUR PATIENT POST TREATMENT</span><span>50</span></li>
    <li><span>MODULE 11: CHEMICAL PEELS</span><span>57</span></li>
    <li><span>MODULE 12: EXTRACTIONS (WITH HYFROTEK)</span><span>58</span></li>
    <li><span>MODULE 13: L.E.D TREATMENT</span><span>49</span></li>
    <li><span>MODULE 14: HAIR REMOVAL</span><span>49</span></li>
    <li><span>MODULE 15: BROAD BAND LIGHT TREATMENT (BBL)</span><span>49</span></li>
    <li><span>MODULE 16: FRACTIONATED LASER (FRACTILUX)</span><span>49</span></li>
  </ul>
  <div class="folio">PAGE : 02</div>
</section>

<section class="page page--toc-b">
  <div class="dots-field" role="img" aria-label="Faint grey dot pattern"></div>
  <h2 class="toc-title">TABLE OF CONTENTS</h2>
  <ul class="toc-list">
    <li><span>MODULE 17: BIOPHOTONIC TREATMENT (LUMIRESCA)</span><span>49</span></li>
    <li><span>MODULE 18: MELACLEAR PEELS</span><span>49</span></li>
    <li><span>MODULE 19: PULSED DYE LASER (VASCUBEAM)</span><span>49</span></li>
    <li><span>MODULE 20: PICO-SECOND LASER (PICO FOR PIGMENT)</span><span>49</span></li>
    <li><span>MODULE 21: PICO-SECOND LASER (PICO TATOO REMOVAL)</span><span>49</span></li>
    <li><span>MODULE 22: RF NEEDLING</span><span>49</span></li>
    <li><span>MODULE 23: SKINQUILL</span><span>49</span></li>
    <li><span>MODULE 24: SKIN TIGHTENING (THERMACORE)</span><span>49</span></li>
    <li><span>MODULE 25: SKIN TIGHTENING (RF TIGHTENING)</span><span>49</span></li>
    <li><span>MODULE 26: CRYOSHAPE</span><span>49</span></li>
    <li><span>MODULE 27: SKIN TAG REMOVAL</span><span>49</span></li>
    <li><span>MODULE 28: SUDREX</span><span>49</span></li>
    <li><span>MODULE 29: PRP</span><span>49</span></li>
    <li><span>MODULE 30: INJECTABLES</span><span>49</span></li>
  </ul>
  <div class="folio">PAGE : 03</div>
</section>

<section class="page page--intro">
  <div class="dots-field" role="img" aria-label="Faint grey dot pattern"></div>
  <h2 class="intro-title">INTRODUCTION</h2>
  <div class="intro-body">
    <p>Welcome to our clinical team! We hope that you enjoy your time as a member of our dermatology team. To assist with your induction, please complete all sections of this workbook and bring it to your progress meet&shy;ings with your manager.</p>
    <p>Links to the theoretical components and exams can be found on our intranet, where we keep all of our reading material and videos.</p>
    <p>All of your practical sheets in this workbook must be signed by an experi&shy;enced member of our team.</p>
    <p>Please also fill out the sign off sheet for each module to ensure that you have completed all components of the module and present to your man&shy;ager for approval to begin treating patients.</p>
    <p class="note">Note: This Workbook Must Remain In A Secure Place At Work, As It Contains Patient. Information And Must Not Be Taken Outside The Practice.</p>
    <p>Progress meetings are highly recommended to make sure you are on the right track before you have completed too many sections and to make sure you are not needing to repeat any work!</p>
    <p>You are expected to have completed modules 1 - 17 within 4 weeks of starting and modules 17 - 27 as arranged with your manager. Modules 28-30 are for nurses only, as arranged with your manager also. Please get busy finding opportunties to complete these sections - enjoy!</p>
  </div>
  <div class="howto">
    <h3>HOW TO FINISH THIS WORKBOOK</h3>
    <ul>
      <li>Read online theory and videos for each module</li>
      <li>Complete online exam for each module</li>
      <li>Complete observations on your sign off sheet</li>
      <li>Complete practical sheets in this workbook</li>
      <li>Present completed sign off sheet to your manager for approval to begin each task</li>
    </ul>
  </div>
  <div class="folio">PAGE : 04</div>
</section>

</body>
</html>
```